Fruits and Vegetables distribution company needs a new eye catching website

We need to get our website up to date. Our clients will look at our website to learn about our products and services. Our design needs to be simple yet impactful to make our brand memorable to our visitors. We need to have somewhere to tell our clients about our history, products and services, our team. We can throw in a few fun facts and figures and maybe some testimonials to impress. We have 4 theme colors that we want to incorporate into the design, you can get in touch for the HEX/RGB codes. Please remember that smooth operation of any animations and interactions is very important.

```html
<!DOCTYPE html>
<html lang="en">
<head>
<meta charset="utf-8">
<title>Harvestia – Fresh Fruits & Vegetables</title>
<link rel="stylesheet" href="https://fonts.googleapis.com/css2?family=Poppins:wght@400;500;600;700&family=Great+Vibes&display=swap">
<style>
:root{
  --orange:#f7a11a;
  --green:#5aa62b;
  --red:#d5281d;
  --ink:#2b2b2b;
  --muted:#8c8c8c;
  --light:#f4f4f4;
  --dark:#1e1e1e;
  --white:#ffffff;
}
*{box-sizing:border-box;margin:0;padding:0}
html,body{width:1200px;height:3607px;overflow:hidden}
body{font-family:'Poppins',sans-serif;color:var(--ink);background:var(--white);position:relative}
.abs{position:absolute}
.btn{position:absolute;background:var(--orange);color:var(--white);font-size:14px;font-weight:600;letter-spacing:2px;text-transform:uppercase;border-radius:22px;display:flex;align-items:center;justify-content:center}
.center{left:0;width:1200px;text-align:center}
/* header */
.topbar{top:14px;right:70px;font-size:13px;display:flex;gap:22px}
.nav{position:absolute;top:96px;left:0;width:1200px;height:24px;font-size:14px}
.nav a{position:absolute;top:0;color:var(--ink);text-decoration:none;white-space:nowrap}
.brand-tab{left:490px;top:0;width:220px;height:175px}
.brand{font-size:24px;font-weight:500;letter-spacing:2px;color:var(--ink)}
.brand-dot{width:40px;height:40px;border-radius:50%;background:var(--red)}
/* hero */
.hero{top:150px;left:0;width:1200px;height:580px;background:radial-gradient(circle at 30% 40%,#e0392b,#a5150f 70%,#7c0e0a)}
.hero-arrow{width:44px;height:44px;border-radius:50%;background:rgba(0,0,0,.55);display:flex;align-items:center;justify-content:center}
.script{font-family:'Great Vibes',cursive;font-size:34px;color:var(--white)}
.hero-title{font-size:36px;font-weight:500;color:var(--white)}
.ghost{position:absolute;border:2px solid var(--white);color:var(--white);font-size:14px;font-weight:600;letter-spacing:2px;border-radius:22px;display:flex;align-items:center;justify-content:center}
/* welcome */
.welcome{top:730px;left:0;width:1200px;height:745px;background:var(--light)}
.promo{background:var(--white);box-shadow:0 2px 8px rgba(0,0,0,.12)}
.promo-label{font-family:'Great Vibes',cursive;font-size:30px;line-height:34px;color:var(--ink);white-space:nowrap}
.promo-strong{font-size:24px;line-height:30px;font-weight:600;color:var(--ink);white-space:nowrap}
.section-title{font-size:32px;font-weight:400;color:var(--ink)}
.section-title b{font-weight:700}
.lead{font-size:15px;line-height:27px;color:var(--muted)}
.feature{font-size:21px;font-weight:700;line-height:28px;text-transform:uppercase}
.feature span{display:block;color:var(--green)}
.ficon{width:62px;height:62px}
/* products */
.products{top:1475px;left:0;width:1200px;height:720px;background:linear-gradient(#f0f0f0,#e6e8ea)}
.prod-card{width:241px;height:222px;background:var(--white);box-shadow:0 2px 6px rgba(0,0,0,.12);display:flex;align-items:center;justify-content:center}
.prod-name{font-size:17px;font-weight:600;text-align:center;width:241px}
.side-arrow{width:36px;height:40px;display:flex;align-items:center;justify-content:center}
/* team */
.team-photo{overflow:hidden}
.team-name{font-size:26px;font-weight:700;letter-spacing:3px;color:var(--ink)}
/* testimonials */
.testi{top:2690px;left:0;width:1200px;height:480px;background:radial-gradient(circle at 55% 45%,#4a2b22,#1c1a17 75%)}
.testi-box{border:1px solid rgba(255,255,255,.25);background:rgba(0,0,0,.25)}
.quote{font-size:17px;line-height:29px;color:var(--white)}
.badge{width:82px;height:82px;border:2px solid rgba(255,255,255,.85);border-radius:50%}
/* footer */
.footer{top:3170px;left:0;width:1200px;height:437px;background:var(--dark);color:var(--white)}
.f-head{font-size:29px;font-weight:600}
.f-links li{list-style:none;font-size:13px;line-height:33px}
.f-links li::before{content:"›";margin-right:14px}
.contact-row{font-size:15px;line-height:25px;display:flex;gap:26px}
.copy{font-size:13px;font-weight:600}
</style>
</head>
<body>

<!-- Header -->
<header>
  <div class="abs topbar">
    <span>&#9990; 1-800 555 0142</span>
    <span>&#9993; info@harvestia.example</span>
  </div>
  <svg class="abs brand-tab" viewBox="0 0 220 175" aria-hidden="true">
    <path d="M0 150 Q60 150 110 175 Q160 150 220 150 L220 0 L0 0Z" fill="#fff"/>
  </svg>
  <nav class="nav">
    <a style="left:158px">Home</a>
    <a style="left:243px">About Us</a>
    <a style="left:353px">Products &amp; Services</a>
    <a style="left:688px">Our Team</a>
    <a style="left:802px">Testimonials</a>
    <a style="left:938px">Contact Us</a>
  </nav>
  <div class="abs brand-dot" style="left:580px;top:30px"></div>
  <div class="abs brand" style="left:0;width:1200px;text-align:center;top:90px">HARVESTIA</div>
  <svg class="abs" style="left:1080px;top:98px" width="50" height="16" viewBox="0 0 50 16" aria-hidden="true">
    <circle cx="7" cy="5" r="3.5" fill="#2b2b2b"/><path d="M1 15 Q7 7 13 15Z" fill="#2b2b2b"/>
    <circle cx="37" cy="7" r="5" stroke="#2b2b2b" stroke-width="2" fill="none"/><line x1="41" y1="11" x2="46" y2="16" stroke="#2b2b2b" stroke-width="2"/>
  </svg>
</header>

<!-- Hero -->
<section class="abs hero" role="img" aria-label="Close-up photograph of fresh red tomatoes"></section>
<svg class="abs" style="left:490px;top:150px" width="220" height="28" viewBox="0 0 220 28" aria-hidden="true"><path d="M0 0 Q60 0 110 25 Q160 0 220 0Z" fill="#fff"/></svg>
<div class="abs hero-arrow" style="left:113px;top:400px"><svg width="12" height="14"><path d="M9 1 L2 7 L9 13" stroke="#fff" stroke-width="3" fill="none"/></svg></div>
<div class="abs hero-arrow" style="left:1036px;top:400px"><svg width="12" height="14"><path d="M3 1 L10 7 L3 13" stroke="#fff" stroke-width="3" fill="none"/></svg></div>
<div class="abs center script" style="top:350px">Lorium ipsum</div>
<h1 class="abs center hero-title" style="top:388px">Finibus Bonorum et Malorum</h1>
<div class="ghost" style="left:515px;top:465px;width:170px;height:44px">LEARN MORE</div>

<!-- Welcome -->
<section class="abs welcome"></section>
<svg class="abs" style="left:470px;top:705px" width="260" height="30" viewBox="0 0 260 30" aria-hidden="true"><path d="M0 30 Q80 30 130 0 Q180 30 260 30Z" fill="#f4f4f4"/></svg>
<div class="abs promo" style="left:70px;top:685px;width:335px;height:188px">
  <div class="abs" role="img" aria-label="Photograph of a pomegranate" style="left:0;top:0;width:190px;height:188px;background:radial-gradient(circle at 45% 55%,#b8202d,#6e0f19 70%,#fff 72%)"></div>
  <div class="abs" style="left:200px;top:82px;width:70px;height:18px;background:var(--orange)"></div>
  <div class="abs promo-label" style="left:232px;top:80px">Fresh</div>
  <div class="abs promo-strong" style="left:232px;top:118px">Fruits</div>
</div>
<div class="abs" style="left:405px;top:770px;width:0;height:0;border-top:22px solid var(--red);border-right:18px solid transparent"></div>
<div class="abs promo" style="left:795px;top:685px;width:333px;height:188px">
  <div class="abs" style="left:20px;top:82px;width:70px;height:18px;background:var(--orange)"></div>
  <div class="abs promo-label" style="left:25px;top:80px">Fresh</div>
  <div class="abs promo-strong" style="left:25px;top:118px">Vegetables</div>
  <div class="abs" role="img" aria-label="Photograph of ripe tomatoes on the vine" style="left:185px;top:0;width:148px;height:188px;background:radial-gradient(circle at 60% 55%,#e2382a,#9e140e 65%,#fff 68%)"></div>
</div>
<div class="abs" style="left:777px;top:770px;width:0;height:0;border-top:22px solid var(--red);border-left:18px solid transparent"></div>
<div class="abs brand-dot" style="left:580px;top:745px"></div>
<div class="abs brand" style="left:0;width:1200px;text-align:center;top:800px">HARVESTIA</div>

<h2 class="abs center section-title" style="top:905px">Welcome To <b>Harvestia</b></h2>
<p class="abs center lead" style="top:965px;left:110px;width:980px">Lorem ipsum dolor sit amet, consectetur adipiscing elit, sed do eiusmod tempor incididunt ut labore et dolore magna aliqua. Ut enim ad minim veniam, quis nostrud exercitation ullamco laboris nisi.</p>

<div class="abs" role="img" aria-label="Wicker basket filled with assorted fresh vegetables" style="left:335px;top:1055px;width:495px;height:295px;border-radius:50% 50% 45% 45%;background:radial-gradient(ellipse at 50% 55%,#c76a2a,#6b8f2a 55%,#f4f4f4 72%)"></div>

<div class="abs feature" style="left:150px;top:1108px;text-align:right;width:102px">100%<span>Organic</span></div>
<svg class="abs ficon" style="left:275px;top:1103px" viewBox="0 0 62 62" aria-hidden="true"><path d="M31 10 C15 10 12 30 18 44 C24 56 38 56 44 44 C50 30 47 10 31 10Z M31 10 V52" stroke="#999" stroke-width="2" fill="none"/></svg>
<div class="abs feature" style="left:110px;top:1246px;text-align:right;width:142px">Family<span>Healthy</span></div>
<svg class="abs ficon" style="left:273px;top:1240px" viewBox="0 0 62 62" aria-hidden="true"><circle cx="22" cy="20" r="8" stroke="#999" stroke-width="2" fill="none"/><circle cx="42" cy="24" r="7" stroke="#999" stroke-width="2" fill="none"/><path d="M8 52 Q22 30 36 52 M30 52 Q42 34 54 52" stroke="#999" stroke-width="2" fill="none"/></svg>
<svg class="abs ficon" style="left:862px;top:1103px" viewBox="0 0 62 62" aria-hidden="true"><circle cx="31" cy="34" r="18" stroke="#999" stroke-width="2" fill="none"/><path d="M23 34 L29 40 L40 28 M31 16 Q34 8 42 8" stroke="#999" stroke-width="2" fill="none"/></svg>
<div class="abs feature" style="left:945px;top:1108px">Guaranteed<span>Products</span></div>
<svg class="abs ficon" style="left:862px;top:1240px" viewBox="0 0 62 62" aria-hidden="true"><rect x="8" y="26" width="46" height="26" stroke="#999" stroke-width="2" fill="none"/><path d="M8 39 H54 M16 26 Q20 12 30 18 Q38 10 46 26" stroke="#999" stroke-width="2" fill="none"/></svg>
<div class="abs feature" style="left:945px;top:1246px">Always<span>Fresh</span></div>

<div class="btn" style="left:515px;top:1377px;width:170px;height:42px">LEARN MORE</div>

<!-- Products -->
<section class="abs products"></section>
<div class="abs" role="img" aria-label="Fresh vegetables arranged along the top edge of a white wooden table" style="left:0;top:1475px;width:1200px;height:150px;background:linear-gradient(90deg,#8cba4a,#e0512a 25%,#f08a2a 45%,#6aa83a 60%,#d8331f 75%,#7fb14a);opacity:.85;-webkit-mask:linear-gradient(#000 40%,transparent);mask:linear-gradient(#000 40%,transparent)"></div>
<h2 class="abs center section-title" style="top:1612px">Products &amp; <b>Services</b></h2>
<p class="abs center lead" style="top:1668px;left:110px;width:980px">Lorem ipsum dolor sit amet, consectetur adipiscing elit, sed do eiusmod tempor incididunt ut labore et dolore magna aliqua. Ut enim ad minim veniam, quis nostrud exercitation ullamco laboris nisi.</p>

<div class="abs prod-card" style="left:72px;top:1770px"><div role="img" aria-label="Photograph of potatoes" style="width:150px;height:130px;border-radius:45%;background:radial-gradient(circle,#c89a62,#8c6234)"></div></div>
<div class="abs prod-card" style="left:344px;top:1770px"><div role="img" aria-label="Photograph of a pumpkin" style="width:125px;height:115px;border-radius:50%;background:radial-gradient(circle,#f7951f,#d9640a)"></div></div>
<div class="abs prod-card" style="left:616px;top:1770px"><div role="img" aria-label="Photograph of halved butternut squash" style="width:170px;height:110px;border-radius:45%;background:radial-gradient(circle,#f29a3a,#d66a18)"></div></div>
<div class="abs prod-card" style="left:887px;top:1770px"><div role="img" aria-label="Photograph of romaine lettuce" style="width:110px;height:160px;border-radius:45%;background:radial-gradient(circle,#d9ecb8,#7fae4a)"></div></div>
<div class="abs prod-name" style="left:72px;top:2010px">POTATO</div>
<div class="abs prod-name" style="left:344px;top:2010px">PUMPKIN</div>
<div class="abs prod-name" style="left:616px;top:2010px">BUTTERNUT</div>
<div class="abs prod-name" style="left:887px;top:2010px">ROMAINE LETTUCE</div>
<div class="abs side-arrow" style="left:0;top:1860px;background:var(--orange)"><svg width="12" height="14"><path d="M9 1 L2 7 L9 13" stroke="#fff" stroke-width="3" fill="none"/></svg></div>
<div class="abs side-arrow" style="left:1164px;top:1860px;background:#9a9a9a"><svg width="12" height="14"><path d="M3 1 L10 7 L3 13" stroke="#fff" stroke-width="3" fill="none"/></svg></div>
<div class="btn" style="left:515px;top:2097px;width:170px;height:42px">VIEW MORE</div>

<!-- Team -->
<h2 class="abs center section-title" style="top:2245px">Our <b>Team</b></h2>
<div class="abs team-photo" role="img" aria-label="Portrait photograph of a smiling team member" style="left:144px;top:2357px;width:210px;height:248px;background:linear-gradient(160deg,#8a6a52,#3c2a22)"></div>
<div class="abs team-photo" role="img" aria-label="Portrait photograph of team member Rosa with a yellow tint" style="left:356px;top:2328px;width:257px;height:302px;background:linear-gradient(160deg,#f6c23a,#d99a0e)"></div>
<div class="abs team-name" style="left:378px;top:2553px">ROSA</div>
<div class="abs team-photo" role="img" aria-label="Portrait photograph of a smiling team member" style="left:616px;top:2357px;width:209px;height:248px;background:linear-gradient(160deg,#cfa98a,#6a4a3a)"></div>
<div class="abs team-photo" role="img" aria-label="Portrait photograph of a smiling team member" style="left:839px;top:2357px;width:214px;height:248px;background:linear-gradient(160deg,#9a7a6a,#2a3a5a)"></div>
<div class="abs side-arrow" style="left:103px;top:2462px;background:var(--orange)"><svg width="12" height="14"><path d="M9 1 L2 7 L9 13" stroke="#fff" stroke-width="3" fill="none"/></svg></div>
<div class="abs side-arrow" style="left:1058px;top:2462px;background:#9a9a9a"><svg width="12" height="14"><path d="M3 1 L10 7 L3 13" stroke="#fff" stroke-width="3" fill="none"/></svg></div>

<!-- Testimonials -->
<section class="abs testi" role="img" aria-label="Dark background photograph of assorted fresh vegetables"></section>
<h2 class="abs center" style="top:2722px;font-size:30px;font-weight:600;color:var(--white)">TESTIMONIALS</h2>
<div class="abs testi-box" style="left:142px;top:2797px;width:902px;height:185px"></div>
<div class="abs" role="img" aria-label="Portrait photograph of customer Nadia" style="left:192px;top:2818px;width:142px;height:142px;border-radius:50%;border:4px solid var(--white);background:radial-gradient(circle,#d9a58a,#7a3a2a)"></div>
<p class="abs quote" style="left:360px;top:2832px;width:620px">“Ut enim ad minima veniam, quis nostrum exercitationem ullam corporis suscipit laboriosam, nisi ut aliquid.</p>
<div class="abs quote" style="left:360px;top:2915px;font-weight:700">- Nadia</div>
<div class="abs badge" style="left:279px;top:3001px"></div>
<div class="abs badge" style="left:392px;top:3001px"></div>
<div class="abs badge" style="left:503px;top:3001px"></div>
<div class="abs badge" style="left:613px;top:3001px"></div>
<div class="abs badge" style="left:724px;top:3001px"></div>
<div class="abs badge" style="left:832px;top:3001px"></div>
<svg class="abs" style="left:575px;top:3115px" width="50" height="24" aria-hidden="true"><path d="M16 2 L6 12 L16 22 M34 2 L44 12 L34 22" stroke="rgba(255,255,255,.6)" stroke-width="2" fill="none"/></svg>

<!-- Footer -->
<footer class="abs footer">
  <div class="abs f-head" style="left:70px;top:78px">Quick Links</div>
  <ul class="abs f-links" style="left:74px;top:137px">
    <li>Home</li><li>About Us</li><li>Products &amp; Services</li><li>Our Team</li><li>Testimonials</li><li>Contact Us</li>
  </ul>
  <div class="abs f-head" style="left:435px;top:78px">Newsletter Subscribe</div>
  <div class="abs" style="left:435px;top:135px;width:330px;height:42px;background:var(--white);color:var(--ink);font-size:14px;font-weight:500;padding:11px 18px">Enter Email Id
    <svg class="abs" style="right:16px;top:15px" width="16" height="12" aria-hidden="true"><rect x="1" y="1" width="14" height="10" stroke="#2b2b2b" fill="none" stroke-width="1.5"/><path d="M1 1 L8 7 L15 1" stroke="#2b2b2b" fill="none" stroke-width="1.5"/></svg>
  </div>
  <div class="btn" style="left:435px;top:195px;width:172px;height:40px">SUBSCRIBE</div>
  <div class="abs" style="left:442px;top:262px;display:flex;gap:20px">
    <span style="width:16px;height:16px;border-radius:50%;background:var(--white)"></span>
    <span style="width:16px;height:16px;background:var(--white)"></span>
    <span style="width:16px;height:16px;border-radius:50%;background:var(--white)"></span>
  </div>
  <div class="abs f-head" style="left:875px;top:78px">Contact us</div>
  <div class="abs contact-row" style="left:875px;top:140px"><svg width="14" height="18" aria-hidden="true"><path d="M7 17 C2 10 1 8 1 6 A6 6 0 0 1 13 6 C13 8 12 10 7 17Z" fill="#fff"/><circle cx="7" cy="6" r="2" fill="#1e1e1e"/></svg><span>214 Orchard Lane,<br>Greenfield, OH 45023</span></div>
  <div class="abs contact-row" style="left:875px;top:222px"><svg width="14" height="16" aria-hidden="true"><path d="M2 1 L5 1 L6 5 L4 6 Q6 10 9 12 L10 10 L14 11 L14 14 Q6 15 2 1Z" fill="#fff"/></svg><span>1-800 555 0178</span></div>
  <div class="abs contact-row" style="left:875px;top:262px"><svg width="14" height="16" aria-hidden="true"><rect x="0" y="3" width="14" height="10" fill="#fff"/><path d="M0 3 L7 9 L14 3" stroke="#1e1e1e" fill="none"/></svg><span>contact@harvestia.example</span></div>
  <div class="abs center copy" style="top:400px">© 2018 &nbsp;|&nbsp; www.harvestia.example</div>
</footer>

</body>
</html>
```